We are looking to create a graphic that will be used in Facebook posts each week to show the daily Porchlight Report. Attached is an example of what we are looking for. We need to be able to update the forecast. So we will need hi-res vector files. The graphics need to represent the level of mosquito activity: SLIGHT, AVERAGE, INTENSE, EXTREME

```html
<!DOCTYPE html>
<html lang="en">
<head>
<meta charset="utf-8">
<title>Greater Lakemont Porchlight Report</title>
<link rel="stylesheet" href="https://fonts.googleapis.com/css2?family=Poppins:wght@400;800&family=Roboto:wght@400;500&display=swap">
<style>
  :root {
    --grass-deep: #3f7a16;
    --grass-mid: #6aa82a;
    --grass-light: #a9d45a;
    --glass: rgba(255, 255, 255, 0.16);
    --glass-edge: rgba(255, 255, 255, 0.32);
    --ink: #ffffff;
    --track: #e6e6e6;
    --green: #2fd11a;
    --yellow: #fdb913;
    --orange: #ef4a23;
    --red: #c8261f;
    --maroon: #7c1712;
    --bug: #b52a22;
  }
  * { box-sizing: border-box; margin: 0; padding: 0; }
  html, body { width: 1200px; height: 675px; overflow: hidden; }
  body { font-family: "Roboto", sans-serif; color: var(--ink); }

  .canvas { position: relative; width: 1200px; height: 675px; overflow: hidden; }

  .backdrop {
    position: absolute; inset: 0;
    background:
      radial-gradient(ellipse at 20% 15%, rgba(220, 240, 160, 0.55), transparent 55%),
      radial-gradient(ellipse at 85% 25%, rgba(190, 225, 120, 0.4), transparent 50%),
      linear-gradient(180deg, var(--grass-light) 0%, var(--grass-mid) 45%, var(--grass-deep) 100%);
  }

  .title { position: absolute; left: 92px; top: 368px; }
  .title-region {
    font-family: "Poppins", sans-serif; font-weight: 400;
    font-size: 22px; letter-spacing: 5px; line-height: 27px;
  }
  .title-name {
    margin-top: 22px;
    font-family: "Poppins", sans-serif; font-weight: 800;
    font-size: 38px; line-height: 45px; letter-spacing: 0.5px;
  }

  .card {
    position: absolute;
    background: var(--glass);
    border: 1px solid var(--glass-edge);
    backdrop-filter: blur(6px);
    text-align: center;
  }
  .card-today { left: 381px; top: 134px; width: 272px; height: 409px; border-radius: 22px; }
  .card-day { width: 131px; height: 197px; border-radius: 16px; }

  .day, .date { font-weight: 400; }
  .card-today .day { margin-top: 47px; font-size: 28px; font-weight: 500; line-height: 34px; }
  .card-today .date { font-size: 28px; line-height: 34px; }
  .card-today .gauge { display: block; width: 158px; height: 158px; margin: 36px auto 0; }
  .card-today .level { margin-top: 34px; font-size: 23px; letter-spacing: 0.5px; }

  .card-day .day { margin-top: 22px; font-size: 14px; font-weight: 500; line-height: 17px; }
  .card-day .date { font-size: 14px; line-height: 17px; }
  .card-day .gauge { display: block; width: 76px; height: 76px; margin: 18px auto 0; }
  .card-day .level { margin-top: 20px; font-size: 11.5px; letter-spacing: 0.4px; }

  .fri { left: 681px; top: 134px; }
  .sat { left: 831px; top: 134px; }
  .sun { left: 980px; top: 134px; }
  .mon { left: 681px; top: 347px; }
  .tue { left: 831px; top: 347px; }
  .wed { left: 980px; top: 347px; }

  .ring { fill: none; stroke-width: 12; }
  .ring-track { stroke: var(--track); }
  .arc { stroke-dasharray: 60 300; }
  .arc-green  { stroke: var(--green);  stroke-dashoffset: 150; }
  .arc-yellow { stroke: var(--yellow); stroke-dashoffset: 90; }
  .arc-orange { stroke: var(--orange); stroke-dashoffset: 30; }
  .arc-red    { stroke: var(--red);    stroke-dashoffset: 330; }
  .arc-maroon { stroke: var(--maroon); stroke-dashoffset: 270; }
  .bug { fill: var(--bug); opacity: 0.85; }
</style>
</head>
<body>
<main class="canvas">
  <div class="backdrop" role="img" aria-label="Close-up photo of dewy green grass blades with soft bokeh"></div>

  <header class="title">
    <div class="title-region">GREATER<br>LAKEMONT</div>
    <h1 class="title-name">PORCHLIGHT<br>REPORT</h1>
  </header>

  <section class="card card-today">
    <div class="day">Thu</div>
    <div class="date">7/21</div>
    <svg class="gauge" viewBox="0 0 100 100">
      <g transform="rotate(-90 50 50)">
        <circle class="ring ring-track" cx="50" cy="50" r="40"/>
        <circle class="ring arc arc-green" cx="50" cy="50" r="40" pathLength="360"/>
        <circle class="ring arc arc-yellow" cx="50" cy="50" r="40" pathLength="360"/>
        <circle class="ring arc arc-orange" cx="50" cy="50" r="40" pathLength="360"/>
        <circle class="ring arc arc-red" cx="50" cy="50" r="40" pathLength="360"/>
        <circle class="ring arc arc-maroon" cx="50" cy="50" r="40" pathLength="360"/>
      </g>
      <circle class="bug" cx="50" cy="50" r="16" role="img" aria-label="Mosquito icon"/>
    </svg>
    <div class="level">EXTREME</div>
  </section>

  <section class="card card-day fri">
    <div class="day">Fri</div>
    <div class="date">7/22</div>
    <svg class="gauge" viewBox="0 0 100 100">
      <g transform="rotate(-90 50 50)">
        <circle class="ring ring-track" cx="50" cy="50" r="40"/>
        <circle class="ring arc arc-green" cx="50" cy="50" r="40" pathLength="360"/>
        <circle class="ring arc arc-yellow" cx="50" cy="50" r="40" pathLength="360"/>
        <circle class="ring arc arc-orange" cx="50" cy="50" r="40" pathLength="360"/>
        <circle class="ring arc arc-red" cx="50" cy="50" r="40" pathLength="360"/>
      </g>
      <circle class="bug" cx="50" cy="50" r="16" role="img" aria-label="Mosquito icon"/>
    </svg>
    <div class="level">INTENSE</div>
  </section>

  <section class="card card-day sat">
    <div class="day">Sat</div>
    <div class="date">7/23</div>
    <svg class="gauge" viewBox="0 0 100 100">
      <g transform="rotate(-90 50 50)">
        <circle class="ring ring-track" cx="50" cy="50" r="40"/>
        <circle class="ring arc arc-green" cx="50" cy="50" r="40" pathLength="360"/>
        <circle class="ring arc arc-yellow" cx="50" cy="50" r="40" pathLength="360"/>
        <circle class="ring arc arc-orange" cx="50" cy="50" r="40" pathLength="360"/>
        <circle class="ring arc arc-red" cx="50" cy="50" r="40" pathLength="360"/>
      </g>
      <circle class="bug" cx="50" cy="50" r="16" role="img" aria-label="Mosquito icon"/>
    </svg>
    <div class="level">INTENSE</div>
  </section>

  <section class="card card-day sun">
    <div class="day">Sun</div>
    <div class="date">7/24</div>
    <svg class="gauge" viewBox="0 0 100 100">
      <g transform="rotate(-90 50 50)">
        <circle class="ring ring-track" cx="50" cy="50" r="40"/>
        <circle class="ring arc arc-green" cx="50" cy="50" r="40" pathLength="360"/>
        <circle class="ring arc arc-yellow" cx="50" cy="50" r="40" pathLength="360"/>
      </g>
      <circle class="bug" cx="50" cy="50" r="16" role="img" aria-label="Mosquito icon"/>
    </svg>
    <div class="level">SLIGHT</div>
  </section>

  <section class="card card-day mon">
    <div class="day">Mon</div>
    <div class="date">7/25</div>
    <svg class="gauge" viewBox="0 0 100 100">
      <g transform="rotate(-90 50 50)">
        <circle class="ring ring-track" cx="50" cy="50" r="40"/>
        <circle class="ring arc arc-green" cx="50" cy="50" r="40" pathLength="360"/>
        <circle class="ring arc arc-yellow" cx="50" cy="50" r="40" pathLength="360"/>
        <circle class="ring arc arc-orange" cx="50" cy="50" r="40" pathLength="360"/>
        <circle class="ring arc arc-red" cx="50" cy="50" r="40" pathLength="360"/>
        <circle class="ring arc arc-maroon" cx="50" cy="50" r="40" pathLength="360"/>
      </g>
      <circle class="bug" cx="50" cy="50" r="16" role="img" aria-label="Mosquito icon"/>
    </svg>
    <div class="level">EXTREME</div>
  </section>

  <section class="card card-day tue">
    <div class="day">Tue</div>
    <div class="date">7/26</div>
    <svg class="gauge" viewBox="0 0 100 100">
      <g transform="rotate(-90 50 50)">
        <circle class="ring ring-track" cx="50" cy="50" r="40"/>
        <circle class="ring arc arc-green" cx="50" cy="50" r="40" pathLength="360"/>
        <circle class="ring arc arc-yellow" cx="50" cy="50" r="40" pathLength="360"/>
      </g>
      <circle class="bug" cx="50" cy="50" r="16" role="img" aria-label="Mosquito icon"/>
    </svg>
    <div class="level">SLIGHT</div>
  </section>

  <section class="card card-day wed">
    <div class="day">Wed</div>
    <div class="date">7/27</div>
    <svg class="gauge" viewBox="0 0 100 100">
      <g transform="rotate(-90 50 50)">
        <circle class="ring ring-track" cx="50" cy="50" r="40"/>
        <circle class="ring arc arc-green" cx="50" cy="50" r="40" pathLength="360"/>
        <circle class="ring arc arc-yellow" cx="50" cy="50" r="40" pathLength="360"/>
        <circle class="ring arc arc-orange" cx="50" cy="50" r="40" pathLength="360"/>
        <circle class="ring arc arc-red" cx="50" cy="50" r="40" pathLength="360"/>
      </g>
      <circle class="bug" cx="50" cy="50" r="16" role="img" aria-label="Mosquito icon"/>
    </svg>
    <div class="level">INTENSE</div>
  </section>
</main>
</body>
</html>
```